Varoden Imports Busisness cards and logo

Varoden imports is a brand new wholesale company located in Londonderry, New Hampshire dedicated to finding unique products from around the world.
Licensed to sell wine and spirits in the state and also authorized distributors of Blue Pepper Design, a manufacturer of girls and women shoes. Other products that we are currently trying to import are cheese and frozen food from Spain.
We would like a design that portraits our diversity of products and wholesale capabilities
Updates

Industry/Entity Type

It Company

```html
<!DOCTYPE html>
<html lang="en">
<head>
<meta charset="utf-8">
<title>Varoden Imports – Business Cards and Logo</title>
<link rel="stylesheet" href="https://fonts.googleapis.com/css2?family=Jura:wght@500;600&family=Tinos&display=swap">
<style>
  :root {
    --stage: #151515;
    --sheet: #ffffff;
    --brand-blue: #1f4fa8;
    --line-blue: #4a78c8;
    --stripe-gray: #9a9a9a;
    --ink: #222428;
    --ink-soft: #3a3d44;
  }
  * { box-sizing: border-box; margin: 0; padding: 0; }
  html, body { width: 1200px; height: 1010px; overflow: hidden; }
  body { background: var(--sheet); font-family: "Jura", sans-serif; color: var(--ink); }

  .showcase { position: relative; width: 1200px; height: 785px; background: var(--stage); }
  .presentation { position: relative; width: 1200px; height: 225px; background: var(--sheet); }

  .card {
    position: absolute; width: 500px; height: 286px; background: var(--sheet);
    overflow: hidden; box-shadow: 0 12px 30px rgba(0,0,0,.55);
  }
  .card--back { left: 80px; top: 250px; }
  .card--front { left: 620px; top: 250px; }

  .corner-stripes { position: absolute; inset: 0; width: 500px; height: 286px; }

  .brand-mark { display: flex; flex-direction: column; align-items: center; position: absolute; }
  .brand-mark__disc { border-radius: 50%; background: var(--brand-blue); }
  .brand-mark__name { font-weight: 600; color: var(--ink); white-space: nowrap; }

  .card--back .brand-mark { left: 40px; top: 62px; width: 210px; }
  .card--back .brand-mark__disc { width: 66px; height: 66px; }
  .card--back .brand-mark__name { font-size: 24px; margin-top: 10px; }

  .divider { position: absolute; left: 272px; top: 62px; width: 1px; height: 160px; background: var(--line-blue); }

  .contact { position: absolute; left: 292px; top: 70px; }
  .contact__name { font-size: 26px; font-weight: 500; letter-spacing: 1px; color: var(--ink); }
  .contact__role { font-size: 13px; font-weight: 500; letter-spacing: 1px; color: var(--ink-soft); margin-top: 2px; }
  .contact__list { list-style: none; margin-top: 16px; font-family: "Tinos", serif; font-size: 12.5px; line-height: 1.7; color: var(--ink); }
  .contact__list li { display: flex; align-items: center; gap: 8px; }
  .contact__list .indent { padding-left: 22px; }
  .icon { width: 14px; height: 14px; flex: none; }

  .card--front .brand-mark { left: 0; top: 50px; width: 500px; }
  .card--front .brand-mark__disc { width: 124px; height: 124px; }
  .card--front .brand-mark__name { font-size: 42px; margin-top: 14px; }

  .logo-sheet .brand-mark { left: 40px; top: 14px; width: 360px; }
  .logo-sheet .brand-mark__disc { width: 136px; height: 136px; }
  .logo-sheet .brand-mark__name { font-size: 44px; margin-top: 10px; }

  .mini { position: absolute; transform-origin: 0 0; transform: scale(.4); }
  .mini .card { position: relative; left: 0; top: 0; box-shadow: 0 8px 20px rgba(0,0,0,.35); }
  .mini--front { left: 712px; top: 862px; }
  .mini--back { left: 912px; top: 818px; }
</style>
</head>
<body>

<section class="showcase">
  <article class="card card--back">
    <svg class="corner-stripes" viewBox="0 0 500 286" aria-hidden="true">
      <polygon points="440,0 500,0 500,60" fill="var(--brand-blue)"/>
      <polygon points="412,0 428,0 500,72 500,88" fill="var(--stripe-gray)"/>
      <polygon points="440,286 500,286 500,226" fill="var(--brand-blue)"/>
      <polygon points="412,286 428,286 500,214 500,198" fill="var(--stripe-gray)"/>
    </svg>
    <div class="brand-mark">
      <span class="brand-mark__disc"></span>
      <span class="brand-mark__name">Varoden imports</span>
    </div>
    <span class="divider"></span>
    <div class="contact">
      <p class="contact__name">Marco R. Delgado</p>
      <p class="contact__role">V.P. of Sales</p>
      <ul class="contact__list">
        <li>
          <svg class="icon" viewBox="0 0 14 14" aria-hidden="true"><rect width="14" height="14" rx="2" fill="var(--brand-blue)"/><rect x="3" y="4" width="8" height="6" fill="none" stroke="#fff" stroke-width="1"/><polyline points="3,4 7,7.5 11,4" fill="none" stroke="#fff" stroke-width="1"/></svg>
          mdelgado@harbornet.net
        </li>
        <li>
          <svg class="icon" viewBox="0 0 14 14" aria-hidden="true"><rect width="14" height="14" rx="2" fill="var(--brand-blue)"/><path d="M7 2.5a3 3 0 0 1 3 3c0 2.2-3 6-3 6s-3-3.8-3-6a3 3 0 0 1 3-3z" fill="#fff"/><circle cx="7" cy="5.5" r="1.1" fill="var(--brand-blue)"/></svg>
          P.O.BOX 418, Millbrook,
        </li>
        <li class="indent">NH 03099-0418 &nbsp;&nbsp;&nbsp; USA</li>
        <li>
          <svg class="icon" viewBox="0 0 14 14" aria-hidden="true"><rect width="14" height="14" rx="2" fill="var(--brand-blue)"/><rect x="4.5" y="2.5" width="5" height="9" rx="1" fill="#fff"/><rect x="5.5" y="3.8" width="3" height="5" fill="var(--brand-blue)"/></svg>
          603-555-0172
        </li>
      </ul>
    </div>
  </article>

  <article class="card card--front">
    <div class="brand-mark">
      <span class="brand-mark__disc"></span>
      <span class="brand-mark__name">Varoden imports</span>
    </div>
  </article>
</section>

<section class="presentation logo-sheet">
  <div class="brand-mark">
    <span class="brand-mark__disc"></span>
    <span class="brand-mark__name">Varoden imports</span>
  </div>
</section>

<div class="mini mini--front">
  <article class="card card--front">
    <div class="brand-mark">
      <span class="brand-mark__disc"></span>
      <span class="brand-mark__name">Varoden imports</span>
    </div>
  </article>
</div>

<div class="mini mini--back">
  <article class="card card--back">
    <svg class="corner-stripes" viewBox="0 0 500 286" aria-hidden="true">
      <polygon points="440,0 500,0 500,60" fill="var(--brand-blue)"/>
      <polygon points="412,0 428,0 500,72 500,88" fill="var(--stripe-gray)"/>
      <polygon points="440,286 500,286 500,226" fill="var(--brand-blue)"/>
      <polygon points="412,286 428,286 500,214 500,198" fill="var(--stripe-gray)"/>
    </svg>
    <div class="brand-mark">
      <span class="brand-mark__disc"></span>
      <span class="brand-mark__name">Varoden imports</span>
    </div>
    <span class="divider"></span>
    <div class="contact">
      <p class="contact__name">Marco R. Delgado</p>
      <p class="contact__role">V.P. of Sales</p>
      <ul class="contact__list">
        <li><svg class="icon" viewBox="0 0 14 14" aria-hidden="true"><rect width="14" height="14" rx="2" fill="var(--brand-blue)"/></svg>mdelgado@harbornet.net</li>
        <li><svg class="icon" viewBox="0 0 14 14" aria-hidden="true"><rect width="14" height="14" rx="2" fill="var(--brand-blue)"/></svg>P.O.BOX 418, Millbrook,</li>
        <li class="indent">NH 03099-0418 &nbsp;&nbsp;&nbsp; USA</li>
        <li><svg class="icon" viewBox="0 0 14 14" aria-hidden="true"><rect width="14" height="14" rx="2" fill="var(--brand-blue)"/></svg>603-555-0172</li>
      </ul>
    </div>
  </article>
</div>

</body>
</html>
```